Laboratory and geotechnical service provider needs Word template

We require a new Word Template for our business. We are looking for a modern, business-like format. We typically generate reports such as management plans, business plans, method statements, technical reports. These reports cover generally between 5 and 30 pages, but sometimes up to 500 pages including the appendices.

Lab reports have their own formats and are not parts of this scope.

Target Market(s)

We report to Clients such as construction industry contractors, governmental departments and engineering consultants.

Industry/Entity Type

Technical Service

Colors

Designer to choose colors to be used in the design.

Requirements
Must have
• The report needs a fancy cover page with a title field, subtitle, project field, client name field, reference number field. Photo/graphics as background on cover. Second page needs a revision table for document control. Table of contents up to 2 levels. Appendices to be part of TOC. Report first page with custom headings for body text, titles, subtitles, headings 1, 2, 3, etc. Include a table with caption, figure with caption, bullet list, numbered list. Appendix page. Please use fonts consistently, choose a common, but professional, modern font.
Nice to have
• We traditionally use black and yellow as company colours. Please visit our company page www.harbentestworks.com.
Should not have
• The two attached word documents is what we use now for your information, we are looking for something better!

```html
<!DOCTYPE html>
<html lang="en">
<head>
<meta charset="utf-8">
<title>Harben Test Works – Report Template</title>
<link rel="stylesheet" href="https://fonts.googleapis.com/css2?family=Montserrat:wght@400;500;600;700&display=swap">
<style>
:root{
  --yellow:#f0dd00;
  --black:#111111;
  --ink:#333333;
  --muted:#8a8a8a;
  --grey:#c9c9c9;
  --grey-light:#e2e2e2;
  --stage:#dcdcdc;
  --paper:#ffffff;
  --photo-top:#9fb3c4;
  --photo-bottom:#7c8a6a;
}
*{box-sizing:border-box;margin:0;padding:0}
html,body{width:1200px;height:3000px;overflow:hidden}
body{position:relative;background:var(--paper);font-family:"Montserrat",Arial,sans-serif;color:var(--ink)}
.stage{position:absolute;left:0;top:0;width:1200px;height:876px;background:var(--stage)}
.page{position:absolute;width:435px;height:614px;background:var(--paper);box-shadow:0 5px 14px rgba(0,0,0,.28);overflow:hidden}
.abs{position:absolute}
.brand-box{position:absolute;background:var(--yellow);display:flex;align-items:center;justify-content:center;text-align:center;font-weight:700;color:var(--black);line-height:1.05;border:1px solid var(--black)}

/* cover */
.cover-art{position:absolute;left:0;top:0}
.cover-title{position:absolute;left:0;width:100%;text-align:center;color:var(--black);font-family:Arial,"Montserrat",sans-serif}
.cover-title .kind{font-size:10.5px}
.cover-title .for{font-size:7px;margin-top:1px}
.cover-title .project{font-size:12.5px;font-weight:700;line-height:1.25;margin-top:2px}
.cover-title .ref{font-size:7.5px;margin-top:2px}
.cover-rule{position:absolute;height:1px;background:var(--yellow)}
.cover-contact{position:absolute;display:flex;justify-content:space-between;font-size:7px;color:var(--black);line-height:1.35}
.cover-contact svg{width:8px;height:8px;vertical-align:-1px;margin-right:3px}
.cover-foot{position:absolute;left:0;bottom:0;width:100%;height:13px}

/* interior */
.head-bar{position:absolute;height:5px;background:var(--yellow)}
.head-line{position:absolute;height:2px;background:var(--black)}
.foot-line{position:absolute;height:2px;background:var(--black)}
.page-no{position:absolute;width:14px;height:9px;background:var(--yellow);font-size:5px;font-weight:700;color:var(--black);display:flex;align-items:center;justify-content:center}

.h1{font-size:11px;font-weight:500;color:var(--black);border-bottom:1px solid var(--yellow);padding-bottom:3px;letter-spacing:.3px}
.toc-row{display:flex;align-items:flex-end;font-size:6px;color:var(--black);margin-top:3px}
.toc-row .lead{flex:1;border-bottom:1px solid var(--black);margin:0 3px 1px}
.toc-row.sub{font-size:5px;color:var(--muted);padding-left:20px}
.toc-row.sub .lead{border-bottom:1px dotted var(--muted)}
.toc-row.sub2{padding-left:46px}
.toc-row.main{font-weight:700}
.toc-row .n{display:inline-block;width:20px}

.rev-table{position:absolute;border-collapse:separate;border-spacing:2px;font-size:6px}
.rev-table td{height:12px;background:var(--grey-light)}
.rev-table tr.labels td{background:var(--black);color:#fff;font-weight:700;padding-left:4px}
.rev-table tr.meta td{background:var(--black);color:#fff;font-size:5px;padding-left:4px}
.rev-table td.blank{background:transparent}

.hs{font-size:7px;color:var(--black);margin-top:6px}
.hs.l3{font-size:6.5px;color:#555}
.hs.l4,.hs.l5{font-size:6.5px;color:var(--muted)}
.cap{font-size:5.5px;font-style:italic;text-align:center;background:var(--grey-light);padding:2px 0;color:var(--black)}
.list{font-size:6.5px;color:var(--black);line-height:1.55}
.body-text{font-size:6.6px;line-height:1.45;color:#444}
</style>
</head>
<body>

<!-- presentation band: cover and back cover, flat -->
<section class="stage">
  <!-- back cover -->
  <div class="page" style="left:628px;top:196px;width:344px;height:492px">
    <svg class="abs" style="left:0;top:0" width="344" height="492" viewBox="0 0 344 492">
      <path d="M0,0 H344 V150 Q200,235 0,110 Z" fill="var(--yellow)"/>
      <path d="M0,110 Q200,235 344,150 V232 Q170,330 0,185 Z" fill="var(--black)"/>
      <polygon points="0,482 175,482 181,492 0,492" fill="var(--yellow)"/>
      <polygon points="175,482 344,482 344,492 181,492" fill="var(--black)"/>
    </svg>
    <div class="brand-box" style="left:136px;top:366px;width:70px;height:55px;font-size:10px">Harben<br>Test<br>Works</div>
  </div>

  <!-- front cover -->
  <div class="page" style="left:228px;top:150px;width:344px;height:492px">
    <svg class="cover-art" width="344" height="492" viewBox="0 0 435 614">
      <defs>
        <linearGradient id="photoTone" x1="0" y1="0" x2="0" y2="1">
          <stop offset="0" stop-color="var(--photo-top)"/>
          <stop offset="1" stop-color="var(--photo-bottom)"/>
        </linearGradient>
      </defs>
      <path d="M0,0 H435 V330 Q230,450 0,300 Z" fill="url(#photoTone)" role="img" aria-label="Photo: laboratory technician at sample shelves and a drilling rig on a city waterfront"/>
      <path d="M0,300 Q230,450 435,330 V345 Q230,460 0,325 Z" fill="var(--black)"/>
      <path d="M332,0 Q260,180 0,245" stroke="var(--yellow)" stroke-width="10" fill="none"/>
      <line x1="30" y1="559" x2="405" y2="559" stroke="var(--yellow)" stroke-width="1.2"/>
      <polygon points="0,601 262,601 270,614 0,614" fill="var(--black)"/>
      <polygon points="262,601 435,601 435,614 270,614" fill="var(--yellow)"/>
    </svg>
    <div class="brand-box" style="left:258px;top:15px;width:68px;height:51px;font-size:9.5px">Harben<br>Test<br>Works</div>
    <div class="cover-title" style="top:348px;transform:scale(.8);transform-origin:top center">
      <div class="kind">STAKEHOLDER MANAGEMENT PLAN</div>
      <div class="for">FOR</div>
      <div class="project">ONSHORE GEOPHYSICAL AND GEOTECHNICAL INVESTIGATION<br>FOR PROJECT C803A</div>
      <div class="ref">DOC. # HT-Oxxxxx-SMP</div>
    </div>
    <div class="cover-contact" style="left:20px;top:453px;width:305px;font-size:5px">
      <div>Harben Test Works Co. WLL<br>P.O. BOX 5180, HARBENPORT</div>
      <div>(+990) 55210480, 55210482<br>(+990) 55210499</div>
      <div>reports@harbentestworks.com</div>
    </div>
  </div>
</section>

<!-- page 1: cover -->
<article class="page" style="left:129px;top:951px">
  <svg class="cover-art" width="435" height="614" viewBox="0 0 435 614">
    <defs>
      <linearGradient id="photoTone2" x1="0" y1="0" x2="0" y2="1">
        <stop offset="0" stop-color="var(--photo-top)"/>
        <stop offset="1" stop-color="var(--photo-bottom)"/>
      </linearGradient>
    </defs>
    <path d="M0,0 H435 V330 Q230,450 0,300 Z" fill="url(#photoTone2)" role="img" aria-label="Photo: laboratory technician at sample shelves and a drilling rig on a city waterfront"/>
    <path d="M0,300 Q230,450 435,330 V345 Q230,460 0,325 Z" fill="var(--black)"/>
    <path d="M332,0 Q260,180 0,245" stroke="var(--yellow)" stroke-width="10" fill="none"/>
    <line x1="30" y1="559" x2="405" y2="559" stroke="var(--yellow)" stroke-width="1.2"/>
    <polygon points="0,601 262,601 270,614 0,614" fill="var(--black)"/>
    <polygon points="262,601 435,601 435,614 270,614" fill="var(--yellow)"/>
  </svg>
  <div class="brand-box" style="left:325px;top:19px;width:87px;height:65px;font-size:12px">Harben<br>Test<br>Works</div>
  <div class="cover-title" style="top:438px">
    <div class="kind">STAKEHOLDER MANAGEMENT PLAN</div>
    <div class="for">FOR</div>
    <div class="project">ONSHORE GEOPHYSICAL AND GEOTECHNICAL INVESTIGATION<br>FOR PROJECT C803A</div>
    <div class="ref">DOC. # HT-Oxxxxx-SMP</div>
  </div>
  <div class="cover-contact" style="left:36px;top:568px;width:370px">
    <div><svg viewBox="0 0 10 10"><path d="M1,5 L5,1 L9,5 V9 H1 Z" fill="none" stroke="#000"/></svg>Harben Test Works Co. WLL<br>&nbsp;&nbsp;&nbsp;P.O. BOX 5180, HARBENPORT</div>
    <div><svg viewBox="0 0 10 10"><circle cx="5" cy="5" r="4" fill="none" stroke="#000"/><path d="M3,3 L4,5 L6,7 L7,6" stroke="#000" fill="none"/></svg>(+990) 55210480, 55210482<br><svg viewBox="0 0 10 10"><rect x="1" y="4" width="8" height="4" fill="none" stroke="#000"/><rect x="3" y="1" width="4" height="3" fill="none" stroke="#000"/></svg>(+990) 55210499</div>
    <div><svg viewBox="0 0 10 10"><rect x="1" y="2" width="8" height="6" fill="none" stroke="#000"/><path d="M1,2 L5,6 L9,2" fill="none" stroke="#000"/></svg>reports@harbentestworks.com</div>
  </div>
</article>

<!-- page 2: revision control -->
<article class="page" style="left:637px;top:951px">
  <div class="brand-box" style="left:20px;top:20px;width:30px;height:22px;font-size:4.5px">Harben<br>Test Works</div>
  <div class="head-bar" style="left:60px;top:25px;width:355px"></div>
  <div class="head-line" style="left:60px;top:31px;width:322px"></div>
  <table class="rev-table" style="left:31px;top:340px;width:370px">
    <tr><td style="width:28px"></td><td style="width:36px"></td><td style="width:160px"></td><td style="width:38px"></td><td style="width:43px"></td><td></td></tr>
    <tr><td></td><td></td><td></td><td></td><td></td><td></td></tr>
    <tr><td></td><td></td><td></td><td></td><td></td><td></td></tr>
    <tr class="labels"><td>Rev</td><td>Date</td><td>Revision Details</td><td>Prepared</td><td>Checked</td><td>Approved</td></tr>
    <tr class="meta"><td class="blank"></td><td class="blank"></td><td class="blank"></td><td colspan="2">Copy no.</td><td></td></tr>
    <tr class="meta"><td class="blank"></td><td class="blank"></td><td class="blank"></td><td colspan="2">Controlled copy &nbsp;&nbsp;&nbsp;&nbsp;&nbsp;YES ☐</td><td style="text-align:right;padding-right:6px">NO ☐</td></tr>
  </table>
  <div class="page-no" style="left:31px;top:593px">1</div>
  <div class="foot-line" style="left:68px;top:596px;width:344px"></div>
</article>

<!-- page 3: contents -->
<article class="page" style="left:129px;top:1620px">
  <div class="head-bar" style="left:22px;top:25px;width:340px"></div>
  <div class="head-line" style="left:50px;top:31px;width:312px"></div>
  <div class="brand-box" style="left:384px;top:20px;width:30px;height:22px;font-size:4.5px">Harben<br>Test Works</div>

  <div class="abs" style="left:37px;top:42px;width:364px">
    <div class="h1">Table of Contents</div>
    <div class="toc-row main"><span class="n">1.</span>HEADING 01<span class="lead"></span>3</div>
    <div class="toc-row sub"><span class="n">1.1.</span>HEADING 02<span class="lead"></span>3</div>
    <div class="toc-row sub sub2"><span class="n">1.1.1.</span>HEADING 03<span class="lead"></span>3</div>
    <div class="toc-row main"><span class="n">2.</span>TABLE STYLE<span class="lead"></span>3</div>
    <div class="toc-row main"><span class="n">3.</span>BULLET LIST<span class="lead"></span>3</div>
    <div class="toc-row sub"><span class="n">3.1.</span>LIST ONE<span class="lead"></span>3</div>
    <div class="toc-row sub"><span class="n">3.2.</span>LIST TWO<span class="lead"></span>3</div>
    <div class="toc-row sub"><span class="n">3.3.</span>LIST THREE<span class="lead"></span>3</div>
    <div class="toc-row sub"><span class="n">3.4.</span>LIST FOUR<span class="lead"></span>3</div>
    <div class="toc-row main"><span class="n">4.</span>BODY TEXT<span class="lead"></span>4</div>
    <div class="toc-row main"><span class="n">5.</span>FIGURES<span class="lead"></span>4</div>
    <div class="toc-row main">APPENDIX A<span class="lead"></span>5</div>
    <div class="toc-row sub" style="padding-left:0">APPENDIX A.1<span class="lead"></span>5</div>
    <div class="toc-row sub sub2">Appendix A.1.1<span class="lead"></span>5</div>

    <div class="h1" style="margin-top:18px">Tables</div>
    <div class="toc-row sub" style="padding-left:0">Table 1: Table style 1<span class="lead"></span>3</div>
    <div class="toc-row sub" style="padding-left:0">Table 2: Table style 2<span class="lead"></span>3</div>

    <div class="h1" style="margin-top:28px">Figures</div>
    <div class="toc-row sub" style="padding-left:0">Figure 1: Picture<span class="lead"></span>4</div>
  </div>

  <div class="foot-line" style="left:24px;top:596px;width:344px"></div>
  <div class="page-no" style="left:388px;top:593px">2</div>
</article>

<!-- page 4: headings, tables, lists -->
<article class="page" style="left:637px;top:1620px">
  <div class="brand-box" style="left:20px;top:20px;width:30px;height:22px;font-size:4.5px">Harben<br>Test Works</div>
  <div class="head-bar" style="left:60px;top:25px;width:355px"></div>
  <div class="head-line" style="left:60px;top:31px;width:322px"></div>

  <div class="abs" style="left:37px;top:42px;width:364px">
    <div class="h1">1.&nbsp; HEADING 01</div>
    <div class="hs">1.1.&nbsp;&nbsp;&nbsp; HEADING 02</div>
    <div class="hs l3">1.1.1.&nbsp;&nbsp;&nbsp; HEADING 03</div>
    <div class="hs l4">1.1.1.1.&nbsp;&nbsp;&nbsp; HEADING 04</div>
    <div class="hs l5">1.1.1.1.1.&nbsp;&nbsp;&nbsp; HEADING 05</div>

    <div class="h1" style="margin-top:14px">2.&nbsp; TABLE STYLE</div>
    <div class="cap" style="margin-top:3px">Table 1: Table style 1</div>
    <div style="height:8px;background:var(--black);margin-top:2px"></div>
    <div style="height:9px;border-bottom:1px solid var(--grey)"></div>
    <div style="height:9px;border-bottom:1px solid var(--grey)"></div>
    <div style="height:9px;border-bottom:1px solid var(--grey)"></div>
    <div class="cap" style="margin-top:10px">Table 2: Table style 2</div>
    <div style="height:7px;background:var(--yellow);margin-top:2px"></div>
    <div style="height:9px;background:var(--grey-light);border-bottom:1px solid #fff"></div>
    <div style="height:9px;background:var(--grey);border-bottom:1px solid #fff"></div>
    <div style="height:9px;background:var(--grey-light);border-bottom:1px solid #fff"></div>
    <div style="height:9px;background:var(--grey)"></div>

    <div class="h1" style="margin-top:14px">3.&nbsp; BULLET LIST</div>
    <div class="list" style="margin-top:4px">
      <div>3.1.&nbsp;&nbsp; List one</div>
      <div style="padding-left:16px">•&nbsp;&nbsp; Bullet</div>
      <div style="padding-left:30px">o&nbsp;&nbsp; bullet<br>o&nbsp;&nbsp; bullet</div>
      <div style="padding-left:16px;line-height:1.25">•&nbsp;&nbsp; bullet<br>•&nbsp;&nbsp; bullet<br>•&nbsp;&nbsp; bullet</div>
      <div>3.2.&nbsp;&nbsp; list two</div>
      <div style="padding-left:14px">✓&nbsp;&nbsp; bullet<br>✓&nbsp;&nbsp; bullet<br>✓&nbsp;&nbsp; bullet</div>
      <div>3.3.&nbsp;&nbsp; List three</div>
      <div>(1). bullet</div>
      <div style="padding-left:12px">(i). bullet</div>
      <div style="padding-left:26px">A). bullet</div>
      <div style="padding-left:40px">a). bullet</div>
      <div style="padding-left:54px">•&nbsp;&nbsp; bullet</div>
      <div>3.4.&nbsp;&nbsp; list four</div>
      <div style="padding-left:26px">⬤&nbsp;&nbsp; bullet<br>⬤&nbsp;&nbsp; bullet<br>⬤&nbsp;&nbsp; bullet</div>
    </div>
  </div>

  <div class="page-no" style="left:31px;top:593px">3</div>
  <div class="foot-line" style="left:68px;top:596px;width:344px"></div>
</article>

<!-- page 5: body text and figure -->
<article class="page" style="left:129px;top:2290px">
  <div class="head-bar" style="left:22px;top:25px;width:340px"></div>
  <div class="head-line" style="left:50px;top:31px;width:312px"></div>
  <div class="brand-box" style="left:384px;top:20px;width:30px;height:22px;font-size:4.5px">Harben<br>Test Works</div>

  <div class="abs" style="left:37px;top:42px;width:364px">
    <div class="h1">4.&nbsp; BODY TEXT</div>
    <p class="body-text" style="margin-top:6px">The report needs a fancy cover page with a title field, subtitle, project field, client name field, reference number field. Photo/graphics as background on cover. Second page needs a revision table for document control. Table of contents up to 2 levels. Appendices to be part of TOC. Report first page with custom headings for body text, titles, subtitles, headings 1, 2, 3, etc. Include a table with caption, figure with caption, bullet list, numbered list. Appendix page. Please use fonts consistently, choose a common, but professional, modern font.</p>
    <div class="hs" style="font-size:6.8px">Sub topic</div>
    <p class="body-text" style="margin-top:4px">The report needs a fancy cover page with a title field, subtitle, project field, client name field, reference number field. Photo/graphics as background on cover. Second page needs a revision table for document control. Table of contents up to 2 levels. Appendices to be part of TOC. Report first page with custom headings for body text, titles, subtitles, headings 1, 2, 3, etc. Include a table with caption, figure with caption, bullet list, numbered list. Appendix page. Please use fonts consistently, choose a common, but professional, modern font.</p>
    <div class="list" style="padding-left:26px;margin-top:3px">⬤&nbsp;&nbsp; bullet<br>⬤&nbsp;&nbsp; bullet<br>⬤&nbsp;&nbsp; bullet</div>

    <div class="h1" style="margin-top:14px">5.&nbsp; FIGURES</div>
    <div class="cap" style="margin-top:14px">Figure 1: Picture</div>
    <div role="img" aria-label="Photo: drilling rig on a city waterfront with palm trees" style="width:230px;height:140px;margin:8px auto 0;background:linear-gradient(180deg,var(--photo-top),var(--photo-bottom))"></div>
  </div>

  <div class="foot-line" style="left:24px;top:596px;width:344px"></div>
  <div class="page-no" style="left:388px;top:593px">4</div>
</article>

<!-- page 6: appendix -->
<article class="page" style="left:637px;top:2290px">
  <div class="brand-box" style="left:20px;top:20px;width:30px;height:22px;font-size:4.5px">Harben<br>Test Works</div>
  <div class="head-bar" style="left:60px;top:25px;width:355px"></div>
  <div class="head-line" style="left:60px;top:31px;width:322px"></div>
  <div class="abs" style="left:37px;top:43px">
    <div style="font-size:10px;color:var(--black)">Appendix A</div>
    <div style="font-size:7px;color:var(--muted);margin-top:8px">Appendix A.1</div>
    <div style="font-size:6.5px;color:var(--muted);margin-top:10px">Appendix A.1.1</div>
  </div>
  <div class="page-no" style="left:31px;top:593px">5</div>
  <div class="foot-line" style="left:68px;top:596px;width:344px"></div>
</article>

</body>
</html>
```